Refresh web site from year 2003

Voltaro Works has a web site (https://vowrk-site.no/) from early 2000 that needs to be refreshed.

Attached are company logo, favicon files, a licensed image to be used, an animation that illustrate the use of one of the products.

Target Market(s)

Industrial customers

Industry/Entity Type

Electrical Switch Board Builders, Automation Industry

Coding

Coded - Design and coding required

Number of Pages Required

3 page

Requirements
Must have
• WordPress site. Use attached animation in the front page (source file is in Adobe Animation format, if adjustments are needed). Product page for two products, "KTR" and "QX-7 Ver B".
Nice to have
• The site should focus on promoting two products KTR and QX-7 Ver B.

```html
<!DOCTYPE html>
<html lang="en">
<head>
<meta charset="utf-8">
<title>Voltaro Works</title>
<link rel="stylesheet" href="https://fonts.googleapis.com/css2?family=Oswald:wght@400;500&family=Roboto:wght@400&display=swap">
<style>
:root{
  --brand:#0d4a86;
  --navy:#1d3e66;
  --footer:#1c2a3e;
  --footer-base:#121a26;
  --body:#555;
  --panel:#f1f1f1;
  --line:#dcdcdc;
  --white:#fff;
}
*{box-sizing:border-box;margin:0;padding:0}
html,body{width:1200px;height:2974px;overflow:hidden;background:var(--white)}
body{position:relative;font-family:"Roboto",Arial,sans-serif;color:var(--body)}
.abs{position:absolute}

.topbar-band{left:0;top:0;width:1200px;height:120px}
.brand{left:66px;top:38px;font-family:"Oswald",sans-serif;font-weight:500;font-size:26px;line-height:1.2;color:var(--brand);display:flex;align-items:center;gap:9px;white-space:nowrap}
.brand-dot{width:12px;height:12px;border-radius:50%;background:var(--brand)}
.contact-block{top:30px;color:var(--white);font-family:"Oswald",sans-serif}
.contact-block .label{font-size:16px;display:flex;align-items:center;gap:9px}
.contact-block .value{font-size:19px;font-weight:500;margin-top:8px;white-space:nowrap}
.divider{top:36px;width:1px;height:46px;background:rgba(255,255,255,.45)}
.lang{left:1082px;top:50px;color:var(--white);font-family:"Oswald",sans-serif;font-size:17px;font-weight:500;display:flex;align-items:center;gap:8px}

.nav{left:0;top:120px;width:1200px;height:56px;border-bottom:1px solid var(--line);display:flex;padding-left:66px}
.nav a{display:flex;align-items:center;justify-content:center;height:56px;font-family:"Oswald",sans-serif;font-size:14px;color:#333;text-decoration:none;border-right:1px solid var(--line);text-transform:uppercase}
.nav a.active{background:var(--brand);color:var(--white)}

.hero{left:0;top:176px;width:1200px;height:415px;background:linear-gradient(90deg,#3a3d40 0%,#55585a 45%,#6f6c66 75%,#5e5c58 100%)}
.hero-title{left:67px;top:220px;width:600px;font-family:"Oswald",sans-serif;font-weight:400;font-size:45px;line-height:52px;color:var(--white)}
.hero-text{left:69px;top:353px;width:490px;font-size:18px;line-height:30px;color:var(--white)}
.btn{display:flex;align-items:center;justify-content:center;background:var(--brand);color:var(--white);font-family:"Oswald",sans-serif;font-size:15px;font-weight:500;text-transform:uppercase;letter-spacing:.3px}
.btn-outline{display:flex;align-items:center;justify-content:center;border:2px solid var(--brand);color:var(--brand);font-family:"Oswald",sans-serif;font-size:13px;font-weight:500;text-transform:uppercase}

.section-title{font-family:"Oswald",sans-serif;font-size:40px;font-weight:500;color:#2b2b2b;line-height:1}
.lead{font-size:18px;line-height:30px;color:#5a5a5a}

.card{top:1273px;width:336px;height:481px;border:2px solid #e6e6e6;background:var(--panel)}
.card-media{position:absolute;left:0;top:0;width:332px;height:186px;background:var(--white)}
.card-photo{position:absolute;left:90px;top:30px;width:140px;height:120px;border-radius:50%;background:radial-gradient(circle at 40% 45%,#eadcdc 0%,#b9a9a9 45%,#2b2b2b 80%,#fff 82%)}
.card-photo.relay{left:90px;top:14px;width:184px;height:160px;border-radius:6px;background:linear-gradient(90deg,#dfe3ea 0 45%,#fff 45% 53%,#2f4a3a 53% 100%)}
.badge{position:absolute;right:14px;top:14px;width:34px;height:26px;border-radius:4px;background:#bdbdbd}
.card-title{position:absolute;left:21px;top:212px;width:280px;font-family:"Oswald",sans-serif;font-weight:400;font-size:24px;line-height:30px;color:#2a2a2a}
.card-text{position:absolute;left:21px;top:290px;width:290px;font-size:16px;line-height:27px;color:#333}
.card-text.muted{font-size:18px;line-height:30px;color:#666}
.card .btn-outline{position:absolute;left:21px;top:403px;width:168px;height:47px}

.services{left:0;top:1943px;width:1200px;height:582px;background:var(--panel)}
.service-icon{top:2203px;width:64px;height:64px}
.service-title{top:2200px;font-family:"Oswald",sans-serif;font-size:24px;color:#2a2a2a}
.service-text{top:2240px;width:260px;font-size:17px;line-height:27px;color:#5a5a5a}

.footer{left:0;top:2525px;width:1200px;height:394px;background:linear-gradient(135deg,var(--footer) 0%,#22344c 60%,var(--footer) 100%)}
.footer-base{left:0;top:2919px;width:1200px;height:55px;background:var(--footer-base)}
.copyright{left:223px;top:2938px;font-family:"Oswald",sans-serif;font-size:13px;color:#c9cfd8}
.footer-head{top:2583px;font-family:"Oswald",sans-serif;font-size:19px;font-weight:500;color:var(--white);text-transform:uppercase}
.footer-list{list-style:none;font-family:"Oswald",sans-serif;font-size:14px;color:#e6eaf0;text-transform:uppercase}
.footer-list li{height:34px;display:flex;align-items:center;gap:12px}
.footer-list li::before{content:">";font-size:12px}
.footer-contact{font-family:"Oswald",sans-serif;font-size:15px;color:#e6eaf0}
.footer-contact div{display:flex;gap:12px;align-items:flex-start;margin-bottom:18px;line-height:27px}
</style>
</head>
<body>

<header>
  <svg class="abs topbar-band" width="1200" height="120" viewBox="0 0 1200 120" aria-hidden="true">
    <polygon points="320,0 1200,0 1200,120 252,120" fill="#1c3f6a"/>
    <polygon points="286,0 300,0 232,120 218,120" fill="#1e4370"/>
    <polygon points="304,0 318,0 250,120 236,120" fill="#2a5a90"/>
  </svg>
  <div class="abs brand"><span class="brand-dot"></span>Voltaro Works</div>

  <div class="abs contact-block" style="left:683px">
    <div class="label">
      <svg width="17" height="17" viewBox="0 0 24 24" aria-hidden="true"><path fill="#fff" d="M6.6 10.8a15.1 15.1 0 0 0 6.6 6.6l2.2-2.2c.3-.3.7-.4 1-.2 1.1.4 2.3.6 3.6.6.6 0 1 .4 1 1V20c0 .6-.4 1-1 1A17 17 0 0 1 3 4c0-.6.4-1 1-1h3.5c.6 0 1 .4 1 1 0 1.3.2 2.5.6 3.6.1.3 0 .7-.2 1z"/></svg>
      Head Office
    </div>
    <div class="value">+47 400 12 345</div>
  </div>
  <div class="abs divider" style="left:832px"></div>
  <div class="abs contact-block" style="left:867px">
    <div class="label">
      <svg width="17" height="13" viewBox="0 0 24 18" aria-hidden="true"><rect x="1" y="1" width="22" height="16" fill="none" stroke="#fff" stroke-width="2"/><path d="M1 1l11 9 11-9" fill="none" stroke="#fff" stroke-width="2"/></svg>
      Email Us
    </div>
    <div class="value">post@voltaroworks.no</div>
  </div>
  <div class="abs divider" style="left:1045px"></div>
  <div class="abs lang">
    <svg width="18" height="18" viewBox="0 0 24 24" aria-hidden="true"><g fill="none" stroke="#fff" stroke-width="2"><circle cx="12" cy="12" r="10"/><ellipse cx="12" cy="12" rx="4.5" ry="10"/><path d="M2 12h20M4 7h16M4 17h16"/></g></svg>
    ENG
  </div>

  <nav class="abs nav">
    <a class="active" style="width:93px">Home</a>
    <a style="width:115px">Services</a>
    <a style="width:121px">Products</a>
    <a style="width:117px">About Us</a>
    <a style="width:110px">Contact</a>
  </nav>
</header>

<section>
  <div class="abs hero" role="img" aria-label="Photograph of an open electrical switchboard with indicator lamps and rotary switches"></div>
  <h1 class="abs hero-title">A reliable and easy way to manage switch signal states</h1>
  <p class="abs hero-text">Lorem ipsum dolor sit amet, consectetur adipiscing elit, sed do eiusmod tempor incididunt ut labore et dolore magna aliqua. Quis ipsum suspendisse ultrices gravida. .</p>
  <div class="abs btn" style="left:68px;top:485px;width:210px;height:54px">Learn More</div>
</section>

<section>
  <h2 class="abs section-title" style="left:66px;top:664px">About Us</h2>
  <p class="abs lead" style="left:66px;top:719px;width:880px">Voltaro Works is a production and development company for electronics with emphasis on small series production. We are today two employees with good and relevant access to additional expertise in the established network. The company was established in 1985 and has since 2001 taken over production equipment and production basis from another company in the same industry.</p>
  <div class="abs btn" style="left:66px;top:881px;width:209px;height:54px">Learn More</div>
</section>

<section>
  <h2 class="abs section-title" style="left:64px;top:1083px">Our Products</h2>
  <p class="abs lead" style="left:66px;top:1131px;width:880px">Lorem ipsum dolor sit amet, consectetur adipiscing elit, sed do eiusmod tempor incididunt ut labore et dolore magna aliqua. Quis ipsum suspendisse ultrices gravida. Risus commodo viverra maecenas accumsan lacus vel facilisis.</p>

  <article class="abs card" style="left:67px">
    <div class="card-media">
      <div class="card-photo" role="img" aria-label="Product photo of a white round indicator lamp"></div>
      <div class="badge" aria-hidden="true"></div>
    </div>
    <h3 class="card-title">Electrical Light Switch Indicator Type KTR</h3>
    <p class="card-text">The Indicator can be used in a switchboard showing switch positions, valve positions etc. for easy reading.</p>
    <div class="btn-outline">More Info</div>
  </article>

  <article class="abs card" style="left:430px">
    <div class="card-media">
      <div class="card-photo" role="img" aria-label="Product photo of a signal lamp with pink dome lens"></div>
      <div class="badge" aria-hidden="true"></div>
    </div>
    <h3 class="card-title">Signal Lamp with built-in LED<br>Type VLX</h3>
    <p class="card-text muted">Lorem ipsum dolor sit amet, consectetur adipiscing elit, ipsum dolor sit amet, consectetur</p>
    <div class="btn-outline">More Info</div>
  </article>

  <article class="abs card" style="left:797px">
    <div class="card-media">
      <div class="card-photo relay" role="img" aria-label="Product photo of an under voltage relay housing and its circuit board"></div>
      <div class="badge" aria-hidden="true"></div>
    </div>
    <h3 class="card-title">Under Voltage Relay</h3>
    <p class="card-text">Interlocking of switch controls the power and transformer stations.</p>
    <div class="btn-outline">More Info</div>
  </article>

  <div class="abs btn" style="left:496px;top:1816px;width:209px;height:54px">All Our Products</div>
</section>

<section>
  <div class="abs services"></div>
  <h2 class="abs section-title" style="left:66px;top:2016px">Our Services</h2>
  <p class="abs lead" style="left:66px;top:2063px;width:800px">Lorem ipsum dolor sit amet, consectetur adipiscing elit, sed do eiusmod tempor incididunt ut labore et dolore magna aliqua. Quis ipsum suspendisse ultrices gravida. Risus commodo viverra maecenas accumsan lacus vel facilisis.</p>

  <svg class="abs service-icon" style="left:66px" viewBox="0 0 64 64" role="img" aria-label="Production icon">
    <rect x="4" y="30" width="56" height="28" rx="4" fill="var(--brand)"/>
    <rect x="10" y="6" width="10" height="26" fill="var(--brand)"/>
    <rect x="10" y="6" width="40" height="8" fill="var(--brand)"/>
    <circle cx="24" cy="44" r="3" fill="#fff"/><circle cx="34" cy="44" r="3" fill="#fff"/><circle cx="44" cy="44" r="3" fill="#fff"/>
  </svg>
  <div class="abs service-title" style="left:157px">Production</div>
  <p class="abs service-text" style="left:157px">Small series production of electronic units in the number of 10 to 200 units.</p>

  <svg class="abs service-icon" style="left:431px" viewBox="0 0 64 64" role="img" aria-label="Development icon">
    <rect x="22" y="4" width="20" height="20" fill="var(--brand)"/>
    <path d="M4 20v18l16 18h8V44L14 30" fill="none" stroke="var(--brand)" stroke-width="6"/>
    <path d="M60 20v18L44 56h-8V44l14-14" fill="none" stroke="var(--brand)" stroke-width="6"/>
  </svg>
  <div class="abs service-title" style="left:517px">Development</div>
  <p class="abs service-text" style="left:517px">Development of product concept to finished product in collaboration with a customer.</p>

  <svg class="abs service-icon" style="left:795px" viewBox="0 0 64 64" role="img" aria-label="Circuit design icon">
    <rect x="0" y="0" width="64" height="64" fill="var(--brand)"/>
    <g stroke="#fff" stroke-width="3" fill="none">
      <path d="M12 64V36l8-8V0M32 64V40M32 24V0M52 64V36l-8-8V0"/>
      <circle cx="32" cy="32" r="6"/>
    </g>
  </svg>
  <div class="abs service-title" style="left:887px">Design</div>
  <p class="abs service-text" style="left:887px">Designing of electronics and print cards for pre-assembled and tested unit.</p>

  <div class="abs btn" style="left:496px;top:2392px;width:209px;height:54px">Learn More</div>
</section>

<footer>
  <div class="abs footer"></div>

  <div class="abs footer-head" style="left:66px">Contact Us</div>
  <div class="abs footer-contact" style="left:67px;top:2630px">
    <div>
      <svg width="15" height="15" viewBox="0 0 24 24" style="margin-top:5px" aria-hidden="true"><path fill="#fff" d="M6.6 10.8a15.1 15.1 0 0 0 6.6 6.6l2.2-2.2c.3-.3.7-.4 1-.2 1.1.4 2.3.6 3.6.6.6 0 1 .4 1 1V20c0 .6-.4 1-1 1A17 17 0 0 1 3 4c0-.6.4-1 1-1h3.5c.6 0 1 .4 1 1 0 1.3.2 2.5.6 3.6.1.3 0 .7-.2 1z"/></svg>
      <span>+47 400 12 345</span>
    </div>
    <div>
      <svg width="17" height="12" viewBox="0 0 24 18" style="margin-top:8px" aria-hidden="true"><rect x="1" y="1" width="22" height="16" fill="none" stroke="#fff" stroke-width="2"/><path d="M1 1l11 9 11-9" fill="none" stroke="#fff" stroke-width="2"/></svg>
      <span>post@voltaroworks.no</span>
    </div>
    <div>
      <svg width="13" height="17" viewBox="0 0 16 22" style="margin-top:5px" aria-hidden="true"><path fill="#fff" d="M8 0a8 8 0 0 0-8 8c0 6 8 14 8 14s8-8 8-14a8 8 0 0 0-8-8zm0 11a3 3 0 1 1 0-6 3 3 0 0 1 0 6z"/></svg>
      <span>Kveldsvegen 48,<br>N-4120 Dalby, Norway</span>
    </div>
  </div>

  <div class="abs footer-head" style="left:340px">Quick Links</div>
  <ul class="abs footer-list" style="left:340px;top:2636px">
    <li>Home</li><li>Services</li><li>Products</li><li>About Us</li><li>Contact</li>
  </ul>

  <div class="abs footer-head" style="left:613px">Products</div>
  <ul class="abs footer-list" style="left:613px;top:2631px">
    <li>Signal Lamp</li><li>Electrical Switch Indicator</li><li>Galvanic Isolation Modules</li><li>Panel Instruments</li><li>Measurement Value Converters</li><li>Under Voltage Relay</li><li>Flame Guard</li>
  </ul>

  <div class="abs footer-base"></div>
  <div class="abs copyright">Copyright © 2003-2021 Voltaro Works.</div>
</footer>

</body>
</html>
```